PowerPoint Template

We would like new powerpoint template for our organization: Fjordvik Data Guild.
Enclosed you find our logo and old template.
Industry/Entity Type
Computer
Requirements
Must have
- 1. Logo
2. Footer (for autor)
3. Font: Variations of ARIAL

```html
<!DOCTYPE html>
<html lang="en">
<head>
<meta charset="utf-8">
<title>Fjordvik Data Guild – Presentation Template</title>
<link href="https://fonts.googleapis.com/css2?family=Ropa+Sans&display=swap" rel="stylesheet">
<style>
  :root {
    --sheet: #000000;
    --paper: #ffffff;
    --paper-shade: #e9e9e9;
    --brand-red: #ed1c24;
    --brand-green: #1b7a5c;
    --brand-blue: #1f4f9c;
    --text-grey: #5a5a5a;
    --rule-grey: #d6d6d6;
    --placeholder: #ececec;
    --placeholder-text: #b4b4b4;
  }
  * { margin: 0; padding: 0; box-sizing: border-box; }
  html, body { width: 1200px; height: 902px; overflow: hidden; background: var(--sheet); }
  body { position: relative; font-family: "Ropa Sans", Arial, sans-serif; color: var(--text-grey); }

  .slide { position: absolute; width: 565px; height: 424px; overflow: hidden;
    background: var(--paper); }
  .slide-bg { position: absolute; inset: 0;
    background: radial-gradient(ellipse at 40% 10%, #e4e4e4 0%, #f4f4f4 45%, #ffffff 70%),
                linear-gradient(#fff, #f2f2f2); background-blend-mode: multiply; }

  .slide--cover-centered { left: 28px; top: 13px; }
  .slide--cover-right { left: 610px; top: 13px; width: 567px; }
  .slide--bullets { left: 28px; top: 450px; }
  .slide--text-images { left: 607px; top: 455px; }

  .cover-band { position: absolute; left: 0; right: 0; bottom: 0; height: 29px;
    background: var(--brand-red); border-top: 3px solid var(--brand-green); }

  .brand { position: absolute; display: flex; flex-direction: column; align-items: center;
    justify-content: center; gap: 8px; text-align: center; }
  .brand-square { width: 54px; height: 54px; background: var(--brand-red); }
  .brand-name { font-size: 15px; line-height: 1.1; color: var(--text-grey); }

  .cover-centered-brand { left: 104px; top: 153px; width: 118px; height: 130px; }
  .cover-divider { position: absolute; left: 246px; top: 153px; width: 1px; height: 130px; background: var(--rule-grey); }
  .cover-title { position: absolute; font-size: 31px; font-weight: 400; color: var(--brand-red); line-height: 1; }
  .cover-lead { position: absolute; font-size: 15px; line-height: 22.6px; }
  .slide--cover-centered .cover-title { left: 269px; top: 186px; }
  .slide--cover-centered .cover-lead { left: 269px; top: 211px; width: 290px; }

  .cover-right-brand { left: 404px; top: 128px; width: 90px; height: 90px; }
  .slide--cover-right .cover-title { right: 17px; top: 231px; text-align: right; }
  .slide--cover-right .cover-lead { right: 17px; top: 268px; width: 290px; text-align: right; }

  .content-title { position: absolute; left: 18px; top: 10px; font-size: 26px; font-weight: 400; color: var(--brand-blue); }
  .content-rule { position: absolute; left: 0; top: 43px; width: 530px; height: 1px;
    background: linear-gradient(90deg, var(--rule-grey), var(--rule-grey) 80%, transparent); }

  .bullet-list { position: absolute; left: 18px; top: 64px; list-style: none; }
  .bullet-list li { display: flex; align-items: center; gap: 7px; height: 34px; font-size: 17px; white-space: nowrap; }
  .bullet-list svg { flex: none; }

  .body-copy { position: absolute; left: 18px; width: 330px; font-size: 13.5px; line-height: 22.6px; }
  .body-copy--first { top: 64px; }
  .body-copy--second { top: 222px; }
  .image-slot { position: absolute; left: 378px; width: 165px; height: 100px; background: var(--placeholder);
    display: flex; align-items: center; justify-content: center; font-size: 14px; color: var(--placeholder-text); }
  .image-slot--first { top: 69px; }
  .image-slot--second { top: 228px; }

  .slide-footer { position: absolute; left: 0; right: 0; bottom: 0; height: 28px;
    background: linear-gradient(#ececec, #dedede); border-top: 2px solid var(--brand-green); }
  .footer-copyright { position: absolute; left: 13px; bottom: 6px; font-size: 14px; color: #444; }
  .footer-brand { position: absolute; left: 491px; bottom: 0; width: 62px; height: 88px;
    background: var(--paper); gap: 5px; }
  .footer-brand .brand-square { width: 26px; height: 26px; }
  .footer-brand .brand-name { font-size: 9px; }
  .slide--text-images .footer-brand { height: 71px; }
</style>
</head>
<body>

<section class="slide slide--cover-centered">
  <div class="slide-bg" role="img" aria-label="Soft grey halftone dot backdrop"></div>
  <div class="brand cover-centered-brand">
    <span class="brand-square"></span>
    <span class="brand-name">Fjordvik Data Guild</span>
  </div>
  <div class="cover-divider"></div>
  <h1 class="cover-title">Project Title Here</h1>
  <p class="cover-lead">Lorem ipsum dolor sit ipsum lorem ipsum dolor sit ipsum Lorem ipsum dolor sit ipsum Lorem ipsum dolor sit ipsum</p>
  <div class="cover-band"></div>
</section>

<section class="slide slide--cover-right">
  <div class="slide-bg" role="img" aria-label="Soft grey halftone dot backdrop"></div>
  <div class="brand cover-right-brand">
    <span class="brand-square"></span>
    <span class="brand-name">Fjordvik Data Guild</span>
  </div>
  <h1 class="cover-title">Project Title Here</h1>
  <p class="cover-lead">Lorem ipsum dolor sit ipsum lorem ipsum dolor sit ipsum Lorem ipsum dolor sit ipsum Lorem ipsum dolor sit ipsum</p>
  <div class="cover-band"></div>
</section>

<section class="slide slide--bullets">
  <h2 class="content-title">Project Title Here</h2>
  <div class="content-rule"></div>
  <ul class="bullet-list">
    <li><svg width="20" height="20" viewBox="0 0 20 20"><path d="M10 1 L19 10 L10 19 L1 10 Z" fill="#ed1c24"/><path d="M8 6 L12 10 L8 14" fill="none" stroke="#fff" stroke-width="2.2"/></svg>Lorem ipsum dolor sit ipsum lorem ipsum dolor sit ipsum Lorem ipsum dolor sit</li>
    <li><svg width="20" height="20" viewBox="0 0 20 20"><path d="M10 1 L19 10 L10 19 L1 10 Z" fill="#ed1c24"/><path d="M8 6 L12 10 L8 14" fill="none" stroke="#fff" stroke-width="2.2"/></svg>Lorem ipsum dolor sit ipsum lorem ipsum dolor sit ipsum Lorem ipsum dolor sit</li>
    <li><svg width="20" height="20" viewBox="0 0 20 20"><path d="M10 1 L19 10 L10 19 L1 10 Z" fill="#ed1c24"/><path d="M8 6 L12 10 L8 14" fill="none" stroke="#fff" stroke-width="2.2"/></svg>Lorem ipsum dolor sit ipsum lorem ipsum dolor sit ipsum Lorem ipsum dolor sit</li>
    <li><svg width="20" height="20" viewBox="0 0 20 20"><path d="M10 1 L19 10 L10 19 L1 10 Z" fill="#ed1c24"/><path d="M8 6 L12 10 L8 14" fill="none" stroke="#fff" stroke-width="2.2"/></svg>Lorem ipsum dolor sit ipsum lorem ipsum dolor sit ipsum Lorem ipsum dolor sit</li>
    <li><svg width="20" height="20" viewBox="0 0 20 20"><path d="M10 1 L19 10 L10 19 L1 10 Z" fill="#ed1c24"/><path d="M8 6 L12 10 L8 14" fill="none" stroke="#fff" stroke-width="2.2"/></svg>Lorem ipsum dolor sit ipsum lorem ipsum dolor sit ipsum Lorem ipsum dolor sit</li>
    <li><svg width="20" height="20" viewBox="0 0 20 20"><path d="M10 1 L19 10 L10 19 L1 10 Z" fill="#ed1c24"/><path d="M8 6 L12 10 L8 14" fill="none" stroke="#fff" stroke-width="2.2"/></svg>Lorem ipsum dolor sit ipsum lorem ipsum dolor sit ipsum Lorem ipsum dolor sit</li>
    <li><svg width="20" height="20" viewBox="0 0 20 20"><path d="M10 1 L19 10 L10 19 L1 10 Z" fill="#ed1c24"/><path d="M8 6 L12 10 L8 14" fill="none" stroke="#fff" stroke-width="2.2"/></svg>Lorem ipsum dolor sit ipsum lorem ipsum dolor sit ipsum Lorem ipsum dolor sit</li>
    <li><svg width="20" height="20" viewBox="0 0 20 20"><path d="M10 1 L19 10 L10 19 L1 10 Z" fill="#ed1c24"/><path d="M8 6 L12 10 L8 14" fill="none" stroke="#fff" stroke-width="2.2"/></svg>Lorem ipsum dolor sit ipsum lorem ipsum dolor sit ipsum Lorem ipsum dolor sit</li>
  </ul>
  <footer class="slide-footer"><span class="footer-copyright">Copyright text here</span></footer>
  <div class="brand footer-brand">
    <span class="brand-square"></span>
    <span class="brand-name">Fjordvik Data Guild</span>
  </div>
</section>

<section class="slide slide--text-images">
  <h2 class="content-title">Project Title Here</h2>
  <div class="content-rule"></div>
  <p class="body-copy body-copy--first">Lorem ipsum dolor sit ipsum lorem ipsum dolor sit ipsum Lorem ipsum dolor sit&nbsp; Lorem ipsum dolor sit ipsum lorem ipsum dolor sit ipsum Lorem ipsum dolor sit Lorem ipsum dolor sit ipsum lorem ipsum dolor sit ipsum Lorem ipsum dolor sit Lorem ipsum dolor sit ipsum lorem ipsum dolor sit ipsum Lorem ipsum dolor sit Lorem ipsum dolor</p>
  <div class="image-slot image-slot--first">IMG HERE</div>
  <p class="body-copy body-copy--second">Lorem ipsum dolor sit ipsum lorem ipsum dolor sit ipsum Lorem ipsum dolor sit&nbsp; Lorem ipsum dolor sit ipsum lorem ipsum dolor sit ipsum Lorem ipsum dolor sit Lorem ipsum dolor sit ipsum lorem ipsum dolor sit ipsum Lorem ipsum dolor sit Lorem ipsum dolor sit ipsum lorem ipsum dolor sit ipsum Lorem ipsum dolor sit Lorem ipsum dolor</p>
  <div class="image-slot image-slot--second">IMG HERE</div>
  <footer class="slide-footer"><span class="footer-copyright">Copyright text here</span></footer>
  <div class="brand footer-brand">
    <span class="brand-square"></span>
    <span class="brand-name">Fjordvik Data Guild</span>
  </div>
</section>

</body>
</html>
```